Consultancy Business Card Design

We need a business card design for a new company based in singapore called FortyOne. FortyOne a boutique consultancy firm offering broad-based business solutions, from conception to re-invention, for ventures from new start-ups to long-running traditional businesses.
Its 2 main divisions (Food & Beverage Operations and Construction & Project Management) have access to a wide range of networks, knowledge bases, and resources to service its clients across numerous diverse sectors. This includes, and is not limited to, construction, F&B, and retail.
We are a company that combines the ambition, boldness and energy of one in the 20s with the dedication, level-headedness and dependability of one entering its 30s. Bridging the experiences of the old with ideals of the young, we draw on the positives of both to create a unique synergy.
We hope to see designs that fits our company profile.
Boutique
Contact Information for Business Card
FortyOne(Company Name)
Marcus Tan (Name)
Principle Consultant (Title)
F&B and Hospitality (Division)
(+65) 8364 5107 (Contact no.)
marcus@fortyone-example.com.sg (Email)
Colors
Designer to choose colors to be used in the design.

```html
<!DOCTYPE html>
<html lang="en">
<head>
<meta charset="utf-8">
<title>FortyOne Business Card</title>
<link href="https://fonts.googleapis.com/css2?family=Montserrat:wght@400;500;600&display=swap" rel="stylesheet">
<style>
  :root {
    --backdrop: #2b2b2b;
    --paper: #f7f7f6;
    --ink: #2e2e2e;
    --accent: #e32525;
  }
  * { box-sizing: border-box; margin: 0; padding: 0; }
  html, body {
    width: 1200px;
    height: 900px;
    overflow: hidden;
    background: var(--backdrop);
    font-family: "Montserrat", Arial, sans-serif;
  }
  .stage {
    width: 1200px;
    height: 900px;
    display: flex;
    flex-direction: column;
    align-items: center;
    justify-content: center;
    gap: 40px;
  }
  .card {
    position: relative;
    width: 700px;
    height: 400px;
    background: var(--paper);
    overflow: hidden;
  }
  .card__band-top {
    position: absolute;
    top: 0; left: 0; right: 0;
    height: 14px;
    background: var(--accent);
  }
  .card__band-bottom {
    position: absolute;
    bottom: 0; left: 0; right: 0;
    height: 6px;
    background: var(--accent);
  }
  .brand {
    position: absolute;
    left: 0; right: 0;
    display: flex;
    justify-content: center;
    align-items: center;
    gap: 16px;
  }
  .card--front .brand { top: 110px; }
  .card--back .brand { top: 178px; }
  .brand__mark {
    width: 14px;
    height: 14px;
    background: var(--accent);
  }
  .brand__name {
    font-weight: 500;
    font-size: 34px;
    letter-spacing: 10px;
    text-transform: uppercase;
    color: var(--ink);
  }

  .contacts {
    position: absolute;
    left: 40px; right: 40px;
    top: 250px;
    display: flex;
    justify-content: space-between;
    align-items: flex-start;
  }
  .contact {
    display: flex;
    flex-direction: column;
    align-items: center;
    text-align: center;
    gap: 12px;
    font-size: 13px;
    line-height: 1.45;
    color: var(--ink);
  }
  .contact--name { align-items: flex-start; text-align: left; }
  .contact--email { align-items: flex-end; text-align: right; }
  .contact__icon {
    width: 30px;
    height: 30px;
    border: 1.5px solid var(--accent);
    display: flex;
    align-items: center;
    justify-content: center;
  }
  .contact__icon svg { width: 16px; height: 16px; fill: var(--accent); }
  .highlight { color: var(--accent); }
</style>
</head>
<body>
<main class="stage">

  <section class="card card--front" aria-label="Business card front">
    <div class="card__band-top"></div>
    <div class="brand">
      <span class="brand__mark" aria-hidden="true"></span>
      <h1 class="brand__name">FortyOne</h1>
    </div>

    <div class="contacts">
      <div class="contact contact--name">
        <span class="contact__icon">
          <svg viewBox="0 0 16 16" aria-hidden="true"><circle cx="8" cy="5" r="3"/><path d="M2 15c0-3.5 2.7-5.5 6-5.5s6 2 6 5.5z"/></svg>
        </span>
        <p>Marcus Tan<br><span class="highlight">Principle Consultant -</span><br>F&amp;B and Hospitality</p>
      </div>

      <div class="contact contact--phone">
        <span class="contact__icon">
          <svg viewBox="0 0 16 16" aria-hidden="true"><path d="M4.2 1.5l2 3-1.4 1.4a8 8 0 0 0 5.3 5.3l1.4-1.4 3 2-1.2 2.4C8 14.4 1.6 8 1.8 2.7z"/></svg>
        </span>
        <p><span class="highlight">(+65)</span> 8364 5107</p>
      </div>

      <div class="contact contact--email">
        <span class="contact__icon">
          <svg viewBox="0 0 16 16" aria-hidden="true"><path d="M1.5 3.5h13v9h-13z M2.5 4.5 8 9l5.5-4.5" fill="none" stroke="#e32525" stroke-width="1.4"/></svg>
        </span>
        <p>marcus<span class="highlight">@fortyone-example.com.sg</span></p>
      </div>
    </div>

    <div class="card__band-bottom"></div>
  </section>

  <section class="card card--back" aria-label="Business card back">
    <div class="card__band-top"></div>
    <div class="brand">
      <span class="brand__mark" aria-hidden="true"></span>
      <p class="brand__name">FortyOne</p>
    </div>
    <div class="card__band-bottom"></div>
  </section>

</main>
</body>
</html>
```